VornaDerm/The experts in permanent hairremoval

Our Brand is VornaDerm and we are specialized on permantent hair removal for the body for men and woman. VornaDerm is working as a Franchise chain.
The brand should be positioned as lifestyle brand but with a medical background. People should trust in us. We take care about their body. This need to be communicated 100%.
Our system is inexpensive but we don't want to show that we are cheap. So we want to communicate that permanent hair removal is a real lifestyle product but affordable.
We already created a logo that you can see the style and colour we prefer.

Target Market(s)

Europe beginning (especially german spoken markets), Middle East, Africa

Industry/Entity Type

Hair Removal

Number of Pages Required

5+ page

Font styles to use
Serif
Other font styles liked:
• Trajan Pro

Requirements
Nice to have
• We are very open for new ideas

```html
<!DOCTYPE html>
<html lang="en">
<head>
<meta charset="utf-8">
<title>VornaDerm – The experts in permanent hair removal</title>
<link href="https://fonts.googleapis.com/css2?family=Cinzel:wght@400;600;700&family=Lora:wght@400;500;700&display=swap" rel="stylesheet">
<style>
:root{
  --blue:#1f78c0;
  --blue-dark:#1a4f86;
  --blue-light:#5fb3e4;
  --ink:#3a3a3a;
  --muted:#777;
  --navy:#1e4a7a;
  --field:#e7ecef;
}
*{margin:0;padding:0;box-sizing:border-box}
html,body{width:735px;height:1200px;overflow:hidden}
body{font-family:"Lora",Georgia,serif;color:var(--ink);background:#fff;position:relative}
.abs{position:absolute}
.display{font-family:"Cinzel","Times New Roman",serif}

/* header */
.header{left:0;top:0;width:735px;height:45px;z-index:5}
.logo{left:147px;top:12px;display:flex;align-items:center;gap:6px}
.logo-dot{width:18px;height:18px;border-radius:50%;background:var(--blue-light)}
.logo-name{font-family:"Cinzel","Times New Roman",serif;font-size:15px;font-weight:400;color:var(--muted)}
.logo-tag{left:172px;top:31px;font-size:4px;color:var(--blue);letter-spacing:.2px;text-transform:uppercase}
.nav{left:292px;top:14px;display:flex;gap:10px;font-size:6.3px;text-transform:uppercase;color:#555}
.nav span{padding:2px 3px}
.nav .active{border:1px solid var(--blue);color:var(--blue)}
.topline{left:412px;top:31px;font-size:5px;color:#555}
.topline b{color:var(--blue);font-weight:500}

/* hero */
.hero{left:0;top:0;width:735px;height:330px;background:linear-gradient(90deg,#b9dcee 0%,#e9f4fa 40%,#f3f9fc 70%,#dbeef7 100%)}
.hero-bgface{left:0;top:0;width:260px;height:330px;background:radial-gradient(ellipse at 40% 40%,#eaf2f6 0%,#c3dfee 60%,rgba(195,223,238,0) 100%)}
.diamond{left:390px;top:60px;width:180px;height:180px;transform:rotate(45deg);background:linear-gradient(135deg,#8fd0f0,#3a9ed8);opacity:.85}
.hero-photo{left:204px;top:82px;width:208px;height:208px;border-radius:50%;border:5px solid #e4f2fa;background:radial-gradient(circle at 45% 40%,#e9d2c4 0%,#c9a592 40%,#5b4138 75%,#2b201c 100%)}
.hero-bubble{left:385px;top:115px;width:148px;height:148px;border-radius:50%;background:radial-gradient(circle at 40% 35%,#2c8ad4,#175fa8);border:4px solid #7cc4ee;color:#fff;font-size:13.5px;line-height:16px;padding:32px 0 0 24px}
.dots{left:356px;top:311px;display:flex;gap:3px}
.dots i{width:5px;height:5px;border-radius:50%;border:1px solid #6a7d8a;display:block}

/* welcome */
.welcome{left:0;top:330px;width:735px;height:275px;background:linear-gradient(90deg,#f3f3f3,#fff 60%)}
.welcome-face{left:470px;top:330px;width:265px;height:275px;clip-path:polygon(0 0,100% 0,100% 100%,64% 100%);background:linear-gradient(160deg,#efd8c8,#dcbba6 60%,#c8a68f)}
.welcome-title{left:147px;top:352px;font-size:13px;font-weight:400;color:#555}
.welcome-title b{font-weight:700;color:#444}
.welcome-img{left:147px;top:378px;width:105px;height:141px;background:linear-gradient(180deg,#8a9aa6,#c9b7ab 50%,#6c7780)}
.care-head{left:260px;top:382px;font-size:8px;color:var(--blue-light)}
.care-lead{left:260px;top:398px;width:152px;font-size:8.5px;line-height:11.5px;color:#444}
.care-body{left:260px;top:440px;width:152px;font-size:5.8px;line-height:7.8px;color:#555}
.care-body p{margin-bottom:6px}
.services-title{left:153px;top:530px;font-size:8px;color:var(--navy)}
.services-sub{left:153px;top:541px;font-size:6.5px;color:var(--blue)}
.services{top:553px;font-size:6.6px;line-height:9.5px;color:#555;list-style:none}
.services li::before{content:"";display:inline-block;width:3px;height:3px;border-radius:50%;background:var(--navy);margin-right:3px;vertical-align:middle}
.doc-mini{left:445px;top:376px;width:45px;height:64px;background:linear-gradient(180deg,#a07a62,#eee 55%,#d9e6ef)}
.sched-title{left:496px;top:401px;font-size:11px;font-weight:700;color:var(--blue-dark)}
.sched-sub{left:496px;top:415px;font-size:7.5px;line-height:9px;color:var(--blue)}
.sched-box{left:437px;top:439px;width:151px;height:140px;background:linear-gradient(180deg,#3d98d6,#7dc0e8);box-shadow:0 2px 5px rgba(0,0,0,.2);color:#fff;padding:8px 6px}
.sched-box .h{font-size:6.8px;font-weight:700}
.sched-box .call{font-size:8.6px;margin-top:5px}
.sched-box .call b{font-weight:700}
.sched-box .s{font-size:5.8px}
.sched-box .visit{font-size:6.8px;margin-top:8px}
.loc{left:437px;width:151px;height:15px;display:flex;align-items:center;font-size:6.2px;color:var(--navy)}
.loc .n{width:20px;height:15px;background:#6a6a6a;color:#fff;display:flex;align-items:center;justify-content:center;margin-right:4px;font-size:8px}
.loc b{font-weight:700}

/* blog */
.blog{left:0;top:605px;width:735px;height:272px;background:linear-gradient(180deg,#cfe7f3,#ddeff8)}
.blog-white{left:0;top:605px;width:735px;height:272px;background:#f7fbfd;clip-path:polygon(0 0,36% 0,0 60%)}
.blog-doctor{left:0;top:605px;width:140px;height:270px;clip-path:polygon(0 0,100% 0,100% 62%,0 100%);background:linear-gradient(180deg,#3a2a22 0%,#c89a7e 25%,#f1f3f5 50%,#e3e9ee 100%)}
.blog-title{left:0;top:612px;width:735px;text-align:center;font-size:13px;font-weight:400;color:#555}
.blog-title b{font-weight:700}
.card{width:215px;height:112px;background:#fff;box-shadow:0 1px 3px rgba(0,0,0,.15)}
.card .ph{position:absolute;left:0;top:0;width:107px;height:112px}
.card .date{position:absolute;left:113px;top:8px;font-size:5.5px;font-weight:700;color:var(--blue-dark)}
.card .t{position:absolute;left:113px;top:17px;width:95px;font-size:6.3px;line-height:7.5px;font-weight:500;color:#555}
.card .ex{position:absolute;left:113px;top:37px;width:95px;font-size:4.5px;line-height:5.6px;color:#888}
.card .read{position:absolute;right:0;bottom:0;width:36px;height:15px;background:var(--navy);color:#fff;font-size:5px;font-weight:700;display:flex;align-items:center;justify-content:center}
.card .ico{position:absolute;top:97px;width:13px;height:15px;display:flex;align-items:center;justify-content:center}
.card .zoom{left:94px;background:#8a8a8a}
.card .heart{left:107px;background:#bfe0f0}

/* contact */
.contact-bg{left:0;top:877px;width:735px;height:323px;background:linear-gradient(180deg,#cfcac6,#b8b0aa)}
.contact-right{left:588px;top:950px;width:147px;height:250px;background:linear-gradient(160deg,#a9d9f2,#2f8fd2);clip-path:polygon(100% 0,100% 100%,0 100%)}
.contact-girl{left:600px;top:950px;width:100px;height:185px;border-radius:40% 40% 30% 30%;background:linear-gradient(180deg,#2e231e,#d7b5a0 35%,#f5f2ef 65%,#d9c1b2)}
.contact-box{left:147px;top:890px;width:441px;height:223px;background:linear-gradient(90deg,#fff 0%,#fff 30%,#d3ecf7 60%,#e7f4fa 100%);box-shadow:0 1px 4px rgba(0,0,0,.2)}
.contact-doc{left:147px;top:890px;width:110px;height:223px;background:linear-gradient(180deg,#5a3a28 0%,#e0bca5 30%,#f2f4f6 55%,#dfe7ed 100%)}
.c-title{left:260px;top:901px;font-size:11.5px;font-weight:700;color:var(--blue-dark)}
.c-city{font-size:8.5px;color:var(--blue-dark);text-transform:uppercase;left:260px}
.c-addr{font-size:5.2px;line-height:6.6px;color:#555;left:260px}
.c-small{left:260px;font-size:5.5px;color:var(--blue-dark)}
.c-val{left:260px;font-size:7.5px;color:#444}
.q-head{left:385px;top:902px;color:var(--blue-dark)}
.q-head .a{font-size:6.5px;font-weight:600}
.q-head .b{font-size:12px;font-weight:700;margin-top:-2px}
.q-text{left:385px;top:925px;width:190px;font-size:5.3px;line-height:7px;color:#666}
.form{left:373px;top:950px;width:215px;height:163px;background:#fff}
.lbl{font-size:4.8px;color:#666;text-transform:uppercase;position:absolute}
.field{position:absolute;background:var(--field);height:17px;width:93px}
.submit{position:absolute;left:12px;top:132px;width:57px;height:15px;background:var(--navy);color:#fff;font-size:5.3px;font-weight:700;display:flex;align-items:center;justify-content:center}

/* social bar */
.social{left:141px;top:1113px;width:453px;height:47px;background:linear-gradient(90deg,#5e514b,#4d423d)}
.social-lbl{left:151px;top:1130px;color:#fff;line-height:9px}
.social-lbl .a{font-size:6px}
.social-lbl .b{font-size:8.5px;font-weight:700}
.soc{top:1121px;width:31px;height:31px;border-radius:50%;background:#cfe8f5;border:2px solid #a9d4ec}
.help{left:384px;top:1126px;color:#fff}
.help .a{font-size:10px;font-weight:700}
.help .b{font-size:6px}
.help-doc{left:532px;top:1107px;width:45px;height:53px;background:linear-gradient(180deg,#6b4a36,#e2c2ae 35%,#f4f4f4 60%,#e9eef2)}

/* footer */
.footer{left:0;top:1160px;width:735px;height:40px;background:linear-gradient(90deg,#b8b0aa,#9e958f)}
.footer-blue{left:480px;top:1160px;width:255px;height:40px;background:linear-gradient(90deg,#7ec3ea,#2f8fd2);clip-path:polygon(18% 0,100% 0,100% 100%,0 100%)}
.f-logo{left:143px;top:1169px;display:flex;align-items:center;gap:5px}
.f-logo .logo-dot{width:14px;height:14px;background:#fff}
.f-logo .logo-name{color:#fff;font-size:12px}
.f-nav{left:242px;top:1172px;font-size:5.6px;color:#fff;word-spacing:1px}
.f-copy{left:242px;top:1181px;font-size:4.8px;color:#eee}
</style>
</head>
<body>

<section class="hero abs" aria-label="Welcome banner"></section>
<div class="hero-bgface abs" role="img" aria-label="Soft faded close-up portrait of a woman in cool blue tones"></div>
<div class="diamond abs" role="img" aria-label="Diamond shaped blue water texture"></div>
<div class="hero-photo abs" role="img" aria-label="Portrait of a young dark-haired woman with smooth skin"></div>
<div class="hero-bubble abs">Are there any<br>Side Effects of<br>Laser Hair<br>Removal<br>Therapy?</div>
<div class="dots abs"><i></i><i></i><i></i></div>

<header class="header abs">
  <div class="logo abs"><span class="logo-dot"></span><span class="logo-name">VornaDerm</span></div>
  <div class="logo-tag abs">The experts in permanent hair removal</div>
  <nav class="nav abs display">
    <span class="active">Home</span><span>Studios</span><span>Prices</span><span>About</span><span>Jobs</span><span>Franchise</span><span>Shop</span><span>Contact</span>
  </nav>
  <div class="topline abs"><b>PHONE:</b> (000) 000-0000 <b>EMAIL:</b> info@vornaderm.com <b>OPEN:</b> 8:00 to 20:00</div>
</header>

<section class="welcome abs"></section>
<div class="welcome-face abs" role="img" aria-label="Close-up of a smiling woman's face"></div>
<h1 class="welcome-title abs display">Welcome to <b>VornaDerm.</b></h1>
<div class="welcome-img abs" role="img" aria-label="Woman with closed eyes receiving a laser treatment"></div>
<div class="care-head abs">Medical Care for Smooth, Hair-free Skin</div>
<p class="care-lead abs">VornaDerm offers advanced, affordable options for permanent hair removal.</p>
<div class="care-body abs">
  <p>With an expert team of trained therapists and medical professionals, VornaDerm is committed to safe, lasting results through personal treatment plans.</p>
  <p>Whether you are tired of shaving, waxing or ingrown hairs, VornaDerm offers gentle treatments for women and men alike. <b>Contact us today!</b></p>
</div>
<div class="services-title abs display">VornaDerm Services</div>
<div class="services-sub abs">Specializing in the following treatments</div>
<ul class="services abs" style="left:147px">
  <li>Diode Laser Hair Removal (Body)</li><li>Facial Hair Removal</li><li>Personal Skin Consultation</li>
</ul>
<ul class="services abs" style="left:287px">
  <li>Treatments for Men</li><li>Full Body Packages</li>
</ul>
<div class="doc-mini abs" role="img" aria-label="Female doctor in a white coat"></div>
<div class="sched-title abs display">Schedule today</div>
<div class="sched-sub abs">and visit one of our<br>three locations.</div>
<div class="sched-box abs">
  <div class="h">Please don't hesitate to call us</div>
  <div class="call">Call <b>000-000-0000</b> to schedule</div>
  <div class="s">your convenient appointment.</div>
  <div class="visit">or visit <b>one of our three locations.</b></div>
  <div class="s">Select your location:</div>
</div>
<div class="loc abs" style="top:520px"><span class="n">1</span><b>ASHFORD</b>&nbsp;LOCATION</div>
<div class="loc abs" style="top:538px"><span class="n">2</span><b>MAPLE RIDGE</b>&nbsp;LOCATION</div>
<div class="loc abs" style="top:556px"><span class="n">3</span><b>LINDEN</b>&nbsp;LOCATION</div>

<section class="blog abs"></section>
<div class="blog-white abs"></div>
<div class="blog-doctor abs" role="img" aria-label="Smiling male doctor with a stethoscope"></div>
<h2 class="blog-title abs display">Read Our <b>Blog</b></h2>

<article class="card abs" style="left:147px;top:637px">
  <div class="ph" role="img" aria-label="Close-up of smooth skin during a treatment" style="background:linear-gradient(135deg,#f2d5c8,#d99a8e 60%,#f0c3cf)"></div>
  <div class="date">JUN 09.2015</div><div class="t">What to expect from your first laser session</div>
  <div class="ex">Your therapist checks your skin and hair type, then sets the laser just for you. Most areas take only a few minutes and feel like a light snap. Mild redness fades within hours, and you can return to your day right away. Avoid sun on the area for a few days.</div>
  <span class="ico zoom"><svg width="6" height="6" viewBox="0 0 10 10"><circle cx="4" cy="4" r="3" fill="none" stroke="#fff" stroke-width="1.6"/><line x1="6" y1="6" x2="9" y2="9" stroke="#fff" stroke-width="1.6"/></svg></span>
  <span class="ico heart"><svg width="6" height="6" viewBox="0 0 10 10"><path d="M5 9 1 5a2.3 2.3 0 0 1 4-3 2.3 2.3 0 0 1 4 3z" fill="#fff"/></svg></span>
  <span class="read">READ</span>
</article>
<article class="card abs" style="left:373px;top:637px">
  <div class="ph" role="img" aria-label="Woman lying down during a facial treatment" style="background:linear-gradient(135deg,#6b5a4c,#c9a590 50%,#5e7a4a)"></div>
  <div class="date">JUN 09.2015</div><div class="t">What to expect from your first laser session</div>
  <div class="ex">Your therapist checks your skin and hair type, then sets the laser just for you. Most areas take only a few minutes and feel like a light snap. Mild redness fades within hours, and you can return to your day right away. Avoid sun on the area for a few days.</div>
  <span class="ico zoom"><svg width="6" height="6" viewBox="0 0 10 10"><circle cx="4" cy="4" r="3" fill="none" stroke="#fff" stroke-width="1.6"/><line x1="6" y1="6" x2="9" y2="9" stroke="#fff" stroke-width="1.6"/></svg></span>
  <span class="ico heart"><svg width="6" height="6" viewBox="0 0 10 10"><path d="M5 9 1 5a2.3 2.3 0 0 1 4-3 2.3 2.3 0 0 1 4 3z" fill="#fff"/></svg></span>
  <span class="read">READ</span>
</article>
<article class="card abs" style="left:147px;top:757px">
  <div class="ph" role="img" aria-label="Profile of a dark-haired woman" style="background:linear-gradient(135deg,#8f8a86,#3a2b25 55%,#caa08c)"></div>
  <div class="date">JUN 09.2015</div><div class="t">What to expect from your first laser session</div>
  <div class="ex">Your therapist checks your skin and hair type, then sets the laser just for you. Most areas take only a few minutes and feel like a light snap. Mild redness fades within hours, and you can return to your day right away. Avoid sun on the area for a few days.</div>
  <span class="ico zoom"><svg width="6" height="6" viewBox="0 0 10 10"><circle cx="4" cy="4" r="3" fill="none" stroke="#fff" stroke-width="1.6"/><line x1="6" y1="6" x2="9" y2="9" stroke="#fff" stroke-width="1.6"/></svg></span>
  <span class="ico heart"><svg width="6" height="6" viewBox="0 0 10 10"><path d="M5 9 1 5a2.3 2.3 0 0 1 4-3 2.3 2.3 0 0 1 4 3z" fill="#fff"/></svg></span>
  <span class="read">READ</span>
</article>
<article class="card abs" style="left:373px;top:757px">
  <div class="ph" role="img" aria-label="Laughing woman with curly blonde hair" style="background:linear-gradient(135deg,#e8e4e0,#d6b08a 50%,#e9cdb8)"></div>
  <div class="date">JUN 09.2015</div><div class="t">What to expect from your first laser session</div>
  <div class="ex">Your therapist checks your skin and hair type, then sets the laser just for you. Most areas take only a few minutes and feel like a light snap. Mild redness fades within hours, and you can return to your day right away. Avoid sun on the area for a few days.</div>
  <span class="ico zoom"><svg width="6" height="6" viewBox="0 0 10 10"><circle cx="4" cy="4" r="3" fill="none" stroke="#fff" stroke-width="1.6"/><line x1="6" y1="6" x2="9" y2="9" stroke="#fff" stroke-width="1.6"/></svg></span>
  <span class="ico heart"><svg width="6" height="6" viewBox="0 0 10 10"><path d="M5 9 1 5a2.3 2.3 0 0 1 4-3 2.3 2.3 0 0 1 4 3z" fill="#fff"/></svg></span>
  <span class="read">READ</span>
</article>

<section class="contact-bg abs" role="img" aria-label="Faded background photo of medical staff"></section>
<div class="contact-right abs"></div>
<div class="contact-girl abs" role="img" aria-label="Woman sitting with smooth bare legs"></div>
<div class="contact-box abs"></div>
<div class="contact-doc abs" role="img" aria-label="Female doctor with glasses and stethoscope"></div>
<h2 class="c-title abs display">Contact Us</h2>
<div class="c-city abs display" style="top:920px">Ashford</div>
<div class="c-addr abs" style="top:932px">Riverbend Health Center<br>214 Elm Street (Suite 12 Area "B")<br>Ashford, PA, 15001</div>
<div class="c-city abs display" style="top:961px">Maple Ridge</div>
<div class="c-addr abs" style="top:973px">Maple Ridge Medical Center<br>Medical Office Building, Suite 201<br>88 N Oak St Ext.<br>Maple Ridge, PA 16002</div>
<div class="c-city abs display" style="top:1013px">Linden</div>
<div class="c-addr abs" style="top:1025px">Westpark Plaza, Suite 110<br>500 Stone Hill Road<br>Lakeview, PA 15003</div>
<div class="c-small abs" style="top:1054px">Phone:</div>
<div class="c-val abs" style="top:1062px">000-000-0000</div>
<div class="c-small abs" style="top:1078px">Email:</div>
<div class="c-val abs" style="top:1086px">info@vornaderm.com</div>

<div class="q-head abs display"><div class="a">GENERAL</div><div class="b">QUESTIONS</div></div>
<p class="q-text abs">If you have general questions, please use the submission form below and a doctor will reply to you within 48 hours.</p>
<form class="form abs">
  <span class="lbl" style="left:12px;top:14px">Your Name</span><span class="field" style="left:12px;top:22px"></span>
  <span class="lbl" style="left:111px;top:14px">Your Email</span><span class="field" style="left:111px;top:22px"></span>
  <span class="lbl" style="left:12px;top:46px">Your Visit Date</span><span class="field" style="left:12px;top:54px"></span>
  <span class="lbl" style="left:111px;top:46px">Your Visit Timing</span><span class="field" style="left:111px;top:54px"></span>
  <span class="lbl" style="left:12px;top:82px">Your Message</span><span class="field" style="left:12px;top:90px;width:192px;height:33px"></span>
  <span class="submit">MY QUESTION!</span>
</form>

<div class="social abs"></div>
<div class="social-lbl abs display"><div class="a">JOIN US ON</div><div class="b">SOCIAL MEDIA</div></div>
<span class="soc abs" style="left:226px" aria-hidden="true"></span>
<span class="soc abs" style="left:261px" aria-hidden="true"></span>
<span class="soc abs" style="left:296px" aria-hidden="true"></span>
<span class="soc abs" style="left:331px" aria-hidden="true"></span>
<div class="help abs"><div class="a display">HELP US, HELP YOU</div><div class="b">Click Here to fill out our Physician Office survey!</div></div>
<div class="help-doc abs" role="img" aria-label="Female doctor in a white coat"></div>

<footer class="footer abs"></footer>
<div class="footer-blue abs"></div>
<div class="f-logo abs"><span class="logo-dot"></span><span class="logo-name">VornaDerm</span></div>
<div class="f-nav abs">Home &nbsp;/&nbsp; Studios &nbsp;/&nbsp; Prices &nbsp;/&nbsp; About &nbsp;/&nbsp; Jobs &nbsp;/&nbsp; Franchise &nbsp;/&nbsp; Shop &nbsp;/&nbsp; Contact</div>
<div class="f-copy abs">2015 VornaDerm - All rights reserved</div>

</body>
</html>
```